Introduction flyer

Bright Orchard Nutrition & Wellness Consulting, is a new holistic nutritional therapy specialising in womens health. I want a flyer that appeals to women between 15 to 60. It must speak "health, food & balance". I have attached the basic info I need included in the text. I like Greens & Blues, soft text. My flyer will be distributed to cafes, shops, fitness centres, hung up in grocery stores & health centres etc. The QEVR & WRUK logos need to appear on the flyer to show I am fully registered. My own logo & company name is attached.

Target Market(s)

Women from 10 to 60 years old.

Industry/Entity Type

Nutritionist

Colors
32a6d7
abd037
33b8a4
fbf289
ffcf3e
b768aa
d5d5d5
dcdcdc
e8e8e8

Requirements
Must have
• An image of healthy food & ladies. A group of women eating soup, stews or curry type dishes, with plenty of colour - no bread or white wine, and not just fruit please. Food that looks enjoyable to the average person.
• Nutrition is main part of my job, so please keep that in mind & emphasise food & natural well being.
Should not have
• People exercising, men, white wine, bread, cakes, sweets etc..

```html
<!DOCTYPE html>
<html lang="en">
<head>
<meta charset="utf-8">
<title>Bright Orchard Nutrition – Introduction Flyer</title>
<link rel="stylesheet" href="https://fonts.googleapis.com/css2?family=Dosis:wght@500;700;800&family=Quicksand:wght@400;500&display=swap">
<style>
  :root{
    --stage:#ffffff;
    --plum:#b768aa;
    --plum-deep:#5e2f68;
    --lime:#abd037;
    --sun:#ffcf3e;
    --sky:#32a6d7;
    --teal:#33b8a4;
    --white:#ffffff;
    --soft-white:#f3e2f0;
    --photo-a:#c9a38a;
    --photo-b:#7f97ab;
  }
  *{box-sizing:border-box;margin:0;padding:0}
  html,body{width:1200px;height:839px;overflow:hidden;background:var(--stage)}
  body{position:relative;font-family:"Quicksand",sans-serif}

  .flyer-side{position:absolute;top:52px;width:522px;height:736px;overflow:hidden}
  .front{left:60px;background:var(--plum)}
  .back{left:612px;background:var(--lime)}
  .deco{position:absolute;inset:0}

  .heading{font-family:"Dosis",sans-serif;font-weight:800;text-transform:uppercase;line-height:.92}

  /* front */
  .brand-badge{position:absolute;left:348px;top:16px;width:138px;height:138px;border-radius:50%;
    background:var(--white);display:flex;flex-direction:column;align-items:center;justify-content:center;
    text-align:center;padding:16px}
  .brand-dot{width:24px;height:24px;border-radius:50%;background:var(--teal);margin-bottom:7px}
  .brand-name{font-family:"Dosis",sans-serif;font-weight:700;font-size:10px;line-height:1.2;color:var(--teal)}

  .question{position:absolute;right:34px;top:286px;text-align:right;color:var(--white);letter-spacing:.3px}
  .question .small{font-size:19px}
  .question .big{font-size:37px}
  .question .mid{font-size:23px}
  .question .last{font-size:42px}
  .question .or{display:inline-block;width:22px;height:22px;border-radius:50%;background:var(--sun);
    color:var(--plum-deep);font-size:11px;line-height:22px;text-align:center;vertical-align:3px;margin-right:5px}

  .intro{position:absolute;left:30px;top:486px;width:225px;color:var(--white)}
  .intro h2{font-size:15px;color:var(--sun);line-height:.98;letter-spacing:.3px}
  .intro h3{font-size:12px;margin:5px 0 8px;font-family:"Dosis",sans-serif;font-weight:800;letter-spacing:.3px}
  .intro p{font-size:9.6px;line-height:1.32;color:var(--soft-white)}

  .credentials{position:absolute;left:28px;top:678px;display:flex;gap:18px}
  .credential{width:70px;height:32px;background:var(--white);border-radius:2px}
  .credential.narrow{width:36px}

  .contact{position:absolute;left:334px;width:176px;color:var(--white)}
  .contact.call{top:516px;font-size:14px}
  .contact.phone{top:532px;font-family:"Dosis",sans-serif;font-weight:800;font-size:22px;color:var(--sky);letter-spacing:.6px}
  .contact.email{top:566px;font-size:14px;line-height:1.15}
  .contact.email b{font-family:"Dosis",sans-serif;font-weight:800;font-size:12.5px;color:var(--sky);letter-spacing:.2px}
  .contact.book{top:606px;font-size:10px;color:var(--sky);line-height:1.3}
  .contact.fine{top:638px;font-size:6.8px;line-height:1.35;color:var(--soft-white)}
  .contact.visits{top:697px;font-size:8.5px;line-height:1.3}

  /* back */
  .problems-title{position:absolute;left:30px;top:50px;color:var(--white);font-size:50px;line-height:.88;letter-spacing:1.5px}
  .problems{position:absolute;left:30px;top:160px;list-style:none;width:360px}
  .problem{font-family:"Dosis",sans-serif;font-weight:800;text-transform:uppercase;font-size:23px;
    line-height:.95;color:var(--white);margin-bottom:21px;letter-spacing:.8px}
  .problem.accent{color:var(--sun)}
  .problem .detail{display:block;font-family:"Quicksand",sans-serif;font-weight:400;text-transform:none;
    font-size:14px;color:var(--white);line-height:1.25;margin-top:4px;letter-spacing:0}
</style>
</head>
<body>

<section class="flyer-side front">
  <svg class="deco" viewBox="0 0 522 736">
    <defs>
      <linearGradient id="photoTone" x1="0" y1="0" x2="1" y2="1">
        <stop offset="0" stop-color="var(--photo-a)"/>
        <stop offset="1" stop-color="var(--photo-b)"/>
      </linearGradient>
    </defs>
    <circle cx="175" cy="130" r="345" fill="none" stroke="var(--sky)" stroke-width="5"/>
    <circle cx="175" cy="130" r="336" fill="var(--sun)"/>
    <circle role="img" aria-label="Photo: two smiling women sharing a colourful healthy meal at a table"
      cx="175" cy="130" r="324" fill="url(#photoTone)"/>
    <circle cx="392" cy="382" r="124" fill="var(--plum-deep)" opacity=".85"/>
    <path d="M430 478 C320 482 300 560 312 688" fill="none"
      stroke="var(--sky)" stroke-width="1.3" stroke-dasharray="4 4"/>
    <path d="M322 688 H522 V736 H322 Z" fill="var(--sky)"/>
  </svg>

  <div class="brand-badge">
    <span class="brand-dot"></span>
    <span class="brand-name">Bright Orchard Nutrition &amp; Wellness Consulting</span>
  </div>

  <div class="question heading">
    <div class="small">Do you experience</div>
    <div class="big">Low energy,</div>
    <div class="big">Low libido,</div>
    <div class="mid">Menstrual cycle</div>
    <div class="mid">complications,</div>
    <div class="mid"><span class="or">OR</span>Are you planning</div>
    <div class="last">A baby?</div>
  </div>

  <div class="intro">
    <h2 class="heading">Small changes to your<br>diet may lead to big<br>changes in your health.</h2>
    <h3>EAT WELL, LIVE WELL.</h3>
    <p>Discover exactly what YOU need to change and how to make these changes long lasting. There is no 'one-fits-all'. My nutritional advice aims to dig up the root cause to my client's health concerns. My lifestyle plans are completely personalised to an individual's needs and circumstances. I consider the whole person not just symptoms or disease.</p>
  </div>

  <div class="credentials">
    <span class="credential" aria-label="QEVR registration badge"></span>
    <span class="credential narrow" aria-label="WRUK registration badge"></span>
  </div>

  <div class="contact call">Call Maeve today on</div>
  <div class="contact phone">085-4270-316</div>
  <div class="contact email">or email <b>MAEVE@<br>BRIGHTORCHARDNUTRITION.IE</b></div>
  <div class="contact book">To book a consultation or for a free no obligation 15 minute consultation.</div>
  <div class="contact fine">Initial consultations last up to 1 hour, follow-ups 30 to 45 minutes. Further tests may be suggested such as blood, urine or saliva checks, agreed with the client in advance.</div>
  <div class="contact visits">Home visits available, at no extra cost within local area. I can visit your place of work or home.</div>
</section>

<section class="flyer-side back">
  <svg class="deco" viewBox="0 0 522 736" aria-hidden="true">
    <circle cx="455" cy="88" r="100" fill="var(--sun)"/>
    <circle cx="474" cy="72" r="98" fill="var(--plum)"/>
    <circle cx="500" cy="705" r="108" fill="var(--plum)"/>
  </svg>

  <h1 class="problems-title heading">List of problems<br>we deal in:</h1>

  <ul class="problems">
    <li class="problem accent">Menstrual cycle<br>challenges
      <span class="detail">(PCOS, Endometriosis, PMS,<br>heavy/irregular periods etc)</span></li>
    <li class="problem">Thyroid conditions</li>
    <li class="problem accent">Low libido</li>
    <li class="problem">Digestive health</li>
    <li class="problem accent">Chronic fatigue syndrome</li>
    <li class="problem">Perimenopause/menopause</li>
    <li class="problem accent">Weight management</li>
    <li class="problem">Perimenopause/menopause</li>
    <li class="problem accent">Type 2 diabetes, blood<br>sugar dysregulation,<br>high blood pressure,<br>high cholesterol</li>
  </ul>
</section>

</body>
</html>
```